Street Sign Project - Attract Customers

We need a street sign designed to display out the front of the building. It design will need to be 1800mm wide x 900mm high. We need to show potential customers where we are inviting. Some of the attachments are for inspiration. The sign will be printed on a sheet of aluminum. if you have a good look at our web site which is www.pk-r.com.au you should get a good feeling about the company and what we do.

Target Market(s)

Construction companies, landscaping and civil earth moving companies who may drive past our business

Industry/Entity Type

Building

Font styles to use
Sans Serif

Colors
ffffff
3277b5
000000

Requirements
Must have
• Company logo must be the main focus point
• The number "54" on the sign to show street number (300mm high)
• phone number - (02) 9418 3065
• web address - www.pk-r.com.au
• I have loaded pictures i would like to see used in the sign
Nice to have
• Banner picture as attached
Should not have
• Bright colours. Please use our blue colour where possible

```html
<!DOCTYPE html>
<html lang="en">
<head>
<meta charset="utf-8">
<title>Street Sign – Carrying &amp; Lifting Works</title>
<link rel="stylesheet" href="https://fonts.googleapis.com/css2?family=Oswald:wght@500&family=Roboto:wght@500;900&display=swap">
<style>
  :root {
    --backdrop: #e6e6e4;
    --sign-dark: #141414;
    --sign-mid: #2a2a2c;
    --white: #ffffff;
    --brand-blue: #3277b5;
    --post: #222222;
  }
  * { margin: 0; padding: 0; box-sizing: border-box; }
  html, body {
    width: 1200px;
    height: 785px;
    overflow: hidden;
    background: var(--backdrop);
  }
  .canvas {
    position: relative;
    width: 1200px;
    height: 785px;
  }
  .street-sign {
    position: absolute;
    left: 50px;
    top: 117px;
    width: 1100px;
    height: 550px;
    overflow: hidden;
    background: linear-gradient(160deg, var(--sign-mid) 0%, var(--sign-dark) 55%, #0c0c0c 100%);
    color: var(--white);
    box-shadow: 0 10px 30px rgba(0,0,0,0.25);
  }
  .photo-strip {
    position: absolute;
    left: 44px;
    top: 26px;
    display: flex;
    gap: 5px;
  }
  .photo-tile {
    width: 112px;
    height: 131px;
  }
  .tile-conveyor { background: linear-gradient(160deg, #8b8f93, #5d6064); }
  .tile-hoist { background: linear-gradient(160deg, #d8dadb, #9ea2a6); }
  .tile-chute { background: linear-gradient(160deg, #6d8fa8, #b9a680); }
  .tile-bin { background: linear-gradient(160deg, #7ea36b, #d5d9cf); }
  .tile-worker { background: linear-gradient(160deg, #c73a32, #a9a2a0); }

  .contact {
    position: absolute;
    right: 44px;
    top: 34px;
    text-align: right;
    font-family: "Roboto", Arial, sans-serif;
    font-weight: 500;
  }
  .contact-phone { font-size: 46px; line-height: 1.1; letter-spacing: 0.5px; }
  .contact-web { font-size: 32px; line-height: 1.1; margin-top: 12px; }

  .street-label {
    position: absolute;
    left: 44px;
    top: 172px;
    font-family: "Oswald", "Arial Narrow", sans-serif;
    font-weight: 500;
    font-size: 44px;
    line-height: 1;
  }
  .street-digits {
    position: absolute;
    left: 36px;
    top: 191px;
    font-family: "Oswald", "Arial Narrow", sans-serif;
    font-weight: 500;
    font-size: 340px;
    line-height: 1;
    letter-spacing: -6px;
  }

  .company-name {
    position: absolute;
    left: 500px;
    top: 228px;
    font-family: "Roboto", Arial, sans-serif;
    font-weight: 900;
    font-size: 96px;
    line-height: 1.05;
    letter-spacing: 1px;
    color: var(--brand-blue);
    text-transform: uppercase;
  }

  .sign-post {
    position: absolute;
    top: 667px;
    width: 36px;
    height: 118px;
    background: var(--post);
  }
  .post-left { left: 380px; }
  .post-right { left: 784px; }
</style>
</head>
<body>
  <main class="canvas">
    <div class="sign-post post-left"></div>
    <div class="sign-post post-right"></div>
    <section class="street-sign">
      <div class="photo-strip">
        <div class="photo-tile tile-conveyor" role="img" aria-label="Photo of an industrial conveyor installation"></div>
        <div class="photo-tile tile-hoist" role="img" aria-label="Photo of a materials hoist on a building site"></div>
        <div class="photo-tile tile-chute" role="img" aria-label="Photo of a rubbish chute on a construction site"></div>
        <div class="photo-tile tile-bin" role="img" aria-label="Photo of a hoisted waste bin"></div>
        <div class="photo-tile tile-worker" role="img" aria-label="Photo of a worker operating hoisting equipment"></div>
      </div>
      <div class="contact">
        <p class="contact-phone">(02) 9418 3065</p>
        <p class="contact-web">www.pk-r.com.au</p>
      </div>
      <p class="street-label">St</p>
      <p class="street-digits">54</p>
      <h1 class="company-name">Carrying<br>&amp; Lifting<br>Works</h1>
    </section>
  </main>
</body>
</html>
```